Quorvex - Automated robotic Inspection with AI need new business cards

We need a new design of our business cards. The company is focused on automated quality control at high speed with unmatched results. We have a logo but need a more forward leaning business card that shows that we are delivering cutting edge technology.

Contact Information for Business Card

Name
Position
Adress
Phone
Email
e.g.
Lena Holmqvist
Chief Financial Officer (CFO)

Quorvex Sweden AB
Bruksvägen 14, SE-175 43 JÄRFÄLLA, Sweden
Mobile: +46735 21 47 83 | Office: +46 8 61 94 27
www.quorvex-example.com

Font styles to use
Sans Serif

```html
<!DOCTYPE html>
<html lang="en">
<head>
<meta charset="utf-8">
<title>Quorvex Business Card</title>
<link rel="stylesheet" href="https://fonts.googleapis.com/css2?family=Bebas+Neue&family=Libre+Franklin:wght@400;600;700&display=swap">
<style>
  :root {
    --brand-blue: #004f7c;
    --arc-grey: #bdbcc0;
    --ink: #222222;
    --paper: #ffffff;
    --backdrop: #dde9f2;
  }
  * { margin: 0; padding: 0; box-sizing: border-box; }
  html, body { width: 1200px; height: 1200px; overflow: hidden; }
  body {
    background: var(--backdrop);
    font-family: "Libre Franklin", Arial, sans-serif;
    position: relative;
  }
  .card {
    position: absolute;
    left: 283px;
    width: 634px;
    height: 362px;
    overflow: hidden;
  }
  .card--front { top: 174px; background: var(--paper); }
  .card--back { top: 610px; background: var(--brand-blue); }

  .wordmark {
    position: absolute;
    display: flex;
    align-items: center;
    font-family: "Libre Franklin", Arial, sans-serif;
    font-weight: 600;
    line-height: 1;
  }
  .wordmark__dot { border-radius: 50%; flex: none; }
  .card--front .wordmark {
    left: 54px; top: 140px;
    font-size: 42px; color: var(--brand-blue); gap: 12px;
  }
  .card--front .wordmark__dot { width: 30px; height: 30px; background: var(--brand-blue); }
  .card--back .wordmark {
    left: 0; right: 0; top: 140px; justify-content: center;
    font-size: 92px; color: var(--paper); gap: 24px;
  }
  .card--back .wordmark__dot { width: 64px; height: 64px; background: var(--paper); }

  .divider {
    position: absolute; left: 317px; top: 71px;
    width: 1px; height: 167px; background: var(--brand-blue);
  }
  .divider::before {
    content: ""; position: absolute; left: 0; top: 0;
    width: 3px; height: 22px; background: var(--brand-blue);
  }

  .contact {
    position: absolute; left: 343px; top: 68px;
    color: var(--ink); font-size: 15.5px; line-height: 20px;
  }
  .contact__name {
    font-family: "Bebas Neue", Impact, sans-serif;
    font-weight: 400; font-size: 32px; line-height: 30px;
    color: var(--brand-blue); letter-spacing: 0.2px;
  }
  .contact__role { margin-top: 0; }
  .contact__company { font-weight: 600; margin-top: 15px; }
  .contact__phones { margin-top: 8px; }
  .contact__label { color: var(--brand-blue); display: inline-block; width: 59px; }

  .footer-arc { position: absolute; left: 0; top: 0; }
  .website {
    position: absolute; left: 0; right: 0; top: 322px;
    text-align: center; color: var(--paper);
    font-size: 17px; letter-spacing: 2px;
  }
  .website strong { font-weight: 700; }
</style>
</head>
<body>
  <section class="card card--front" aria-label="Business card front">
    <div class="wordmark"><span class="wordmark__dot"></span><span>Quorvex</span></div>
    <div class="divider"></div>
    <div class="contact">
      <h1 class="contact__name">Lena Holmqvist</h1>
      <p class="contact__role">Chief Financial Officer (CFO)</p>
      <p class="contact__company">Quorvex Sweden AB</p>
      <p>Bruksvägen 14, SE-175 43 JÄRFÄLLA,<br>Sweden</p>
      <p class="contact__phones"><span class="contact__label">Mobile:</span> +46735 21 47 83<br><span class="contact__label">Office:</span> +46 8 61 94 27</p>
    </div>
    <svg class="footer-arc" width="634" height="362" viewBox="0 0 634 362">
      <path d="M66,318 Q317,237 501,318 Q317,256 66,318 Z" fill="var(--arc-grey)"/>
      <path d="M66,318 Q317,237 568,318 Q317,256 66,318 Z" fill="var(--arc-grey)"/>
      <path d="M0,346.5 Q317,243.5 634,346.5 L634,362 L0,362 Z" fill="var(--brand-blue)"/>
    </svg>
    <p class="website">www.<strong>quorvex-example</strong>.com</p>
  </section>

  <section class="card card--back" aria-label="Business card back">
    <div class="wordmark"><span class="wordmark__dot"></span><span>Quorvex</span></div>
  </section>
</body>
</html>
```